Need 4 childhood cancer facts posters

Hello. I run a nonprofit in East Tennessee, USA that supports children with cancer and their families.

I need 4 poster designs with facts about childhood cancers. It should either have pictures of children with cancer or be focused around the whole idea of childhood cancer awareness. This project will require time and research. I will post links to facts as the project goes forward.

Questions can be emailed to tmerrow@glowwithnora.org. AI format of our logo has been uploaded. I have images and links here http://www.glowwithnora.org/contest-pics.html

You can also view our website at www.glowwithnora.org

Some facts: http://pelt.tumorstats.example/archive/publications/childhood/

USE THESE FACTS: * Everyday, approximately 250 children will die from childhood cancer. *Childhood Cancers is the number 1 cause of death in children under age 15 in the US. *Less than 5% of the federal governments budget toward cancer research is dedicated to childhood cancers. *One in 330 children will be diagnosed with cancer by the time they are 20.

Poster will be 24 inches wide by 36 inches tall.

```html
<!DOCTYPE html>
<html lang="en">
<head>
<meta charset="utf-8">
<title>Childhood Cancer Awareness Poster</title>
<link rel="stylesheet" href="https://fonts.googleapis.com/css2?family=Ubuntu:wght@400;500;700&display=swap">
<style>
  :root {
    --paper-light: #f7f7f7;
    --paper-mid: #e6e6e6;
    --paper-shade: #cfcfcf;
    --charcoal: #464646;
    --band: #3d3d3f;
    --lime: #c9c83c;
    --white: #ffffff;
  }
  html, body {
    margin: 0;
    padding: 0;
    width: 788px;
    height: 1200px;
    overflow: hidden;
    background: var(--paper-mid);
  }
  .poster {
    position: relative;
    width: 788px;
    height: 1200px;
    overflow: hidden;
    font-family: "Ubuntu", sans-serif;
    background: linear-gradient(90deg, var(--paper-shade) 0%, var(--paper-mid) 8%, var(--paper-light) 55%, var(--paper-mid) 100%);
  }
  .headline {
    position: absolute;
    margin: 0;
    font-weight: 700;
    color: var(--charcoal);
    line-height: 1;
    letter-spacing: -1px;
  }
  .headline--everyday { left: 108px; top: 196px; font-size: 106px; }
  .headline--will-die { left: 108px; top: 506px; font-size: 112px; }
  .stat-band {
    position: absolute;
    left: 0;
    top: 296px;
    width: 684px;
    height: 206px;
    background: var(--band);
  }
  .stat-band__lead {
    position: absolute;
    left: 112px;
    top: 32px;
    font-size: 28px;
    font-weight: 400;
    color: var(--white);
  }
  .stat-band__number {
    position: absolute;
    right: 18px;
    top: 4px;
    font-size: 150px;
    font-weight: 700;
    line-height: 1;
    color: var(--lime);
    letter-spacing: -2px;
  }
  .stat-band__noun {
    position: absolute;
    right: 24px;
    top: 142px;
    font-size: 54px;
    font-weight: 700;
    line-height: 1;
    color: var(--lime);
  }
  .cause-highlight {
    position: absolute;
    left: 104px;
    top: 618px;
    height: 54px;
    padding: 0 10px;
    background: var(--lime);
    font-size: 43px;
    font-weight: 700;
    line-height: 54px;
    color: var(--charcoal);
  }
  .foundation {
    position: absolute;
    left: 250px;
    top: 880px;
    display: flex;
    align-items: center;
    gap: 14px;
  }
  .foundation__dot {
    width: 22px;
    height: 22px;
    border-radius: 50%;
    background: var(--lime);
    flex: none;
  }
  .foundation__name {
    font-size: 24px;
    font-weight: 500;
    line-height: 1.25;
    color: var(--charcoal);
  }
  .corner-stripes {
    position: absolute;
    right: 0;
    bottom: 0;
    width: 788px;
    height: 1200px;
  }
</style>
</head>
<body>
  <main class="poster">
    <svg class="corner-stripes" viewBox="0 0 788 1200" aria-hidden="true">
      <polygon points="788,962 788,1012 470,1200 392,1200" fill="var(--band)"/>
      <polygon points="788,1034 788,1200 508,1200" fill="var(--lime)"/>
    </svg>

    <h1 class="headline headline--everyday">EVERYDAY</h1>

    <div class="stat-band">
      <span class="stat-band__lead">approximately</span>
      <span class="stat-band__number">250</span>
      <span class="stat-band__noun">CHILDREN</span>
    </div>

    <p class="headline headline--will-die">WILL DIE</p>

    <p class="cause-highlight" style="margin:0">from childhood cancer.</p>

    <div class="foundation">
      <span class="foundation__dot"></span>
      <span class="foundation__name">Nora Whitfield<br>Childhood Cancer Foundation</span>
    </div>
  </main>
</body>
</html>
```